KTR Engineering Pty Ltd

I have already had Corvale welding and fabrication cards made , my business has changed too KTR engineering Pty Ltd so I need my logo changed on the cards
one side have my logo then the other side have what we do.
front side logo and details
owner /operator : Lachlan Meravic
email: ktr.works@ironvalemail.com
number: 0491537204
ABN: 47 261 538 902
ACN: 718 352 946
on back have in dot points what we do:
* structural steel erection
* precast panels
* site welding
*steel alteration & repair
* rigging & dogging
*labour hire
all details in breif

```html
<!DOCTYPE html>
<html lang="en">
<head>
<meta charset="utf-8">
<title>KTR Engineering Pty Ltd – Business Card</title>
<link href="https://fonts.googleapis.com/css2?family=Inter:wght@400;700;800&display=swap" rel="stylesheet">
<style>
  :root {
    --bg: #e6e6e6;
    --card: #f6f6f7;
    --navy: #172636;
    --rust: #9a3f35;
    --ink: #222629;
    --grey: #4c4f53;
  }
  * { margin: 0; padding: 0; box-sizing: border-box; }
  html, body { width: 1200px; height: 1200px; overflow: hidden; }
  body {
    background: var(--bg);
    font-family: "Inter", Arial, sans-serif;
    display: flex;
    flex-direction: column;
    align-items: center;
    justify-content: center;
    gap: 60px;
  }
  .card {
    position: relative;
    width: 880px;
    height: 503px;
    background: var(--card);
    border-radius: 30px;
    box-shadow: 0 2px 4px rgba(0,0,0,0.08);
  }
  /* Front */
  .owner { position: absolute; left: 60px; top: 128px; }
  .owner-name { font-size: 31px; font-weight: 700; color: var(--navy); letter-spacing: -0.2px; }
  .owner-role { font-size: 20px; font-weight: 400; color: var(--rust); margin-top: 2px; }
  .rule { position: absolute; left: 60px; top: 212px; width: 560px; height: 2px; background: var(--navy); }
  .brand {
    position: absolute;
    display: flex;
    align-items: center;
    gap: 14px;
  }
  .brand-mark { width: 22px; height: 22px; background: var(--rust); flex: none; }
  .brand-name {
    font-weight: 800;
    color: var(--navy);
    line-height: 1.05;
    text-transform: uppercase;
    letter-spacing: 0.5px;
  }
  .card-front .brand { right: 60px; top: 136px; }
  .card-front .brand-name { font-size: 28px; }
  .contact { position: absolute; left: 60px; top: 402px; font-size: 21px; color: var(--ink); line-height: 28px; }
  .contact-row { display: flex; align-items: center; gap: 10px; }
  .contact-row svg { width: 18px; height: 18px; flex: none; }
  .registration { position: absolute; right: 60px; top: 404px; font-size: 21px; color: var(--ink); line-height: 28px; text-align: right; }
  /* Back */
  .card-back .brand { left: 70px; top: 218px; }
  .card-back .brand-name { font-size: 30px; }
  .divider { position: absolute; left: 471px; top: 168px; width: 2px; height: 188px; background: var(--grey); }
  .services { position: absolute; left: 500px; top: 162px; list-style: none; }
  .services li { font-size: 22px; color: var(--grey); line-height: 32.5px; display: flex; align-items: center; gap: 14px; }
  .services li::before { content: ""; width: 9px; height: 9px; border-radius: 50%; background: var(--navy); }
</style>
</head>
<body>
  <section class="card card-front">
    <div class="owner">
      <div class="owner-name">Lachlan Meravic</div>
      <div class="owner-role">owner /operator</div>
    </div>
    <div class="rule"></div>
    <div class="brand">
      <span class="brand-mark"></span>
      <span class="brand-name">KTR Engineering<br>Pty Ltd</span>
    </div>
    <div class="contact">
      <div class="contact-row">
        <svg viewBox="0 0 24 24"><path fill="#172636" d="M6.6 10.8a15.1 15.1 0 0 0 6.6 6.6l2.2-2.2c.3-.3.7-.4 1-.2 1.1.4 2.3.6 3.6.6.6 0 1 .4 1 1V20c0 .6-.4 1-1 1A17 17 0 0 1 3 4c0-.6.4-1 1-1h3.5c.6 0 1 .4 1 1 0 1.3.2 2.5.6 3.6.1.3 0 .7-.2 1z"/></svg>
        <span>0491537204</span>
      </div>
      <div class="contact-row">
        <svg viewBox="0 0 24 24"><path fill="#172636" d="M3 6h18v12H3z"/><path fill="none" stroke="#f6f6f7" stroke-width="1.8" d="M3.5 6.5 12 13l8.5-6.5"/></svg>
        <span>ktr.works@ironvalemail.com</span>
      </div>
    </div>
    <div class="registration">
      <div>ABN: 47 261 538 902</div>
      <div>ACN: 718 352 946</div>
    </div>
  </section>

  <section class="card card-back">
    <div class="brand">
      <span class="brand-mark"></span>
      <span class="brand-name">KTR Engineering<br>Pty Ltd</span>
    </div>
    <div class="divider"></div>
    <ul class="services">
      <li>Structural steel erection</li>
      <li>Precast panels</li>
      <li>Site welding</li>
      <li>Steel alteration &amp; repair</li>
      <li>Rigging &amp; dogging</li>
      <li>Labour hire</li>
    </ul>
  </section>
</body>
</html>
```